" Minha empresa basicamente funciona da seguinte forma, visito os clientes, pego todas as ideias (Briefing), levo para a empresa, elaboramos o melhor projeto possivel para aquele cliente, apresentamos o projeto, o cliente aprovando, começamos a fabricação. E estamos sempre envolvidos em eventos para trazer tecnologia para nossos clientes. "

```html
<!DOCTYPE html>
<html lang="pt-BR">
<head>
<meta charset="utf-8">
<title>Veltrano – Papel Timbrado</title>
<link rel="stylesheet" href="https://fonts.googleapis.com/css2?family=Montserrat:wght@400;500;700&family=Open+Sans:wght@400&display=swap">
<style>
  :root {
    --backdrop: #e9e7e4;
    --paper: #ffffff;
    --ink-dark: #333335;
    --ink-body: #5a5a5c;
    --ink-soft: #9a9a9c;
    --accent-tan: #c7a77f;
    --band-dark: #3a3a3d;
    --rule: #d6d6d6;
  }
  * { box-sizing: border-box; margin: 0; padding: 0; }
  html, body { width: 1200px; height: 1200px; overflow: hidden; background: var(--backdrop); }
  .letterhead {
    position: absolute; left: 204px; top: 40px;
    width: 792px; height: 1120px;
    background: var(--paper);
    box-shadow: 0 6px 24px rgba(0,0,0,.12);
    font-family: "Open Sans", sans-serif;
    color: var(--ink-body);
    overflow: hidden;
  }
  .brand {
    position: absolute; top: 78px; left: 0; right: 0;
    display: flex; flex-direction: column; align-items: center; gap: 12px;
  }
  .brand-square { width: 26px; height: 26px; background: var(--accent-tan); }
  .brand-name {
    font-family: "Montserrat", sans-serif; font-weight: 500;
    font-size: 26px; letter-spacing: 3px; color: var(--accent-tan);
  }
  .headline {
    position: absolute; top: 210px; left: 0; right: 0; text-align: center;
  }
  .headline-title {
    font-family: "Montserrat", sans-serif; font-weight: 700;
    font-size: 34px; letter-spacing: 5px; color: var(--ink-dark);
  }
  .headline-sub {
    margin-top: 8px;
    font-family: "Montserrat", sans-serif; font-weight: 500;
    font-size: 14px; letter-spacing: 4px; color: var(--ink-dark);
  }
  .headline-rule {
    width: 90px; height: 2px; background: var(--ink-dark); margin: 18px auto 0;
  }
  .body-copy {
    position: absolute; top: 370px; left: 96px; right: 96px;
    font-size: 13px; line-height: 1.6; text-align: justify;
  }
  .body-copy p + p { margin-top: 22px; }
  .signoff {
    position: absolute; top: 770px; right: 96px; width: 140px;
    text-align: center; font-size: 13px;
  }
  .signoff-mark {
    position: relative; margin-top: 14px; height: 96px;
  }
  .signoff-seal {
    position: absolute; left: 6px; top: 8px; width: 78px; height: 78px;
    border: 2px solid #8fa3c4; border-radius: 50%;
  }
  .signoff-signature {
    position: absolute; left: 40px; top: 26px; width: 96px; height: 44px;
    background: linear-gradient(90deg, rgba(60,70,110,.15), rgba(60,70,110,.35), rgba(60,70,110,.12));
    border-radius: 22px;
  }
  .footer-rule {
    position: absolute; left: 96px; right: 0; top: 980px; height: 1px; background: var(--rule);
  }
  .footer-band {
    position: absolute; left: 0; right: 0; bottom: 0; height: 110px;
  }
  .band-shape { position: absolute; left: 0; top: 0; width: 792px; height: 110px; }
  .contacts {
    position: absolute; left: 420px; right: 30px; bottom: 20px;
    display: grid; grid-template-columns: 1fr 1.4fr; row-gap: 10px; column-gap: 20px;
    font-size: 12px; line-height: 17px; color: #ffffff;
  }
  .contact-item { display: flex; align-items: center; gap: 8px; white-space: nowrap; }
  .contact-icon { width: 13px; height: 13px; flex: none; display: block; }
</style>
</head>
<body>
  <main class="letterhead">
    <header class="brand">
      <span class="brand-square"></span>
      <span class="brand-name">VELTRANO</span>
    </header>

    <section class="headline">
      <h1 class="headline-title">PAPER MOCKUP</h1>
      <p class="headline-sub">PSD RESOURCE BY PAPERLINE</p>
      <div class="headline-rule"></div>
    </section>

    <section class="body-copy">
      <p>Lorem ipsum dolor sit amet, consectetur adipiscing elit. Donec orci purus, luctus vitae dignissim eu, iaculis sed purus. Vivamus faucibus, ipsum nec aliquet viverra, leo mauris condimentum ante, ultrices in suscipit a, tempus non massa. Phasellus nec eros mauris, et scelerisque orci.</p>
      <p>Donec malesuada orci vitae nulla accumsan porta a id massa. Quisque accumsan iaculis magna sit amet fringilla. Maecenas commodo, magna eget tincidunt semper, odio nibh rutrum mi, id feugiat ante nisi eu nisi. Vestibulum nunc orci, rhoncus a placerat in, ultrices in mi.</p>
      <p>Sed id augue vitae urna euismod commodo aliquet a quam. Pellentesque arcu ante, cursus et malesuada ut, consequat et diam. Nullam erat sem, rhoncus et ullamcorper vitae, rhoncus et arcu. Fusce aliquet faucibus ultricies. Morbi semper, est in tincidunt gravida, quis nisl.</p>
    </section>

    <aside class="signoff">
      <p>Sincerely,</p>
      <div class="signoff-mark">
        <span class="signoff-seal"></span>
        <span class="signoff-signature" role="img" aria-label="Handwritten signature"></span>
      </div>
    </aside>

    <div class="footer-rule"></div>

    <footer class="footer-band">
      <svg class="band-shape" viewBox="0 0 792 110" preserveAspectRatio="none">
        <polygon points="330,26 420,26 400,110 310,110" fill="var(--accent-tan)"/>
        <polygon points="400,26 792,26 792,110 380,110" fill="var(--band-dark)"/>
      </svg>
      <div class="contacts">
        <span class="contact-item">
          <svg class="contact-icon" viewBox="0 0 24 24"><path fill="#fff" d="M6.6 10.8a15 15 0 0 0 6.6 6.6l2.2-2.2a1 1 0 0 1 1-.25 11.4 11.4 0 0 0 3.6.57 1 1 0 0 1 1 1V20a1 1 0 0 1-1 1A17 17 0 0 1 3 4a1 1 0 0 1 1-1h3.5a1 1 0 0 1 1 1c0 1.25.2 2.45.57 3.57a1 1 0 0 1-.25 1z"/></svg>
          (11) 90000-1234
        </span>
        <span class="contact-item">
          <svg class="contact-icon" viewBox="0 0 24 24"><path fill="none" stroke="#fff" stroke-width="2" d="M3 5h18v14H3zM3 6l9 7 9-7"/></svg>
          contato@veltrano.com.br
        </span>
        <span class="contact-item">
          <svg class="contact-icon" viewBox="0 0 24 24"><path fill="#fff" d="M6.6 10.8a15 15 0 0 0 6.6 6.6l2.2-2.2a1 1 0 0 1 1-.25 11.4 11.4 0 0 0 3.6.57 1 1 0 0 1 1 1V20a1 1 0 0 1-1 1A17 17 0 0 1 3 4a1 1 0 0 1 1-1h3.5a1 1 0 0 1 1 1c0 1.25.2 2.45.57 3.57a1 1 0 0 1-.25 1z"/></svg>
          (11) 90000-5678
        </span>
        <span class="contact-item">
          <svg class="contact-icon" viewBox="0 0 24 24"><circle cx="12" cy="12" r="9" fill="none" stroke="#fff" stroke-width="2"/><path fill="none" stroke="#fff" stroke-width="2" d="M3 12h18M12 3c3 3 3 15 0 18M12 3c-3 3-3 15 0 18"/></svg>
          www.veltrano.com.br
        </span>
      </div>
    </footer>
  </main>
</body>
</html>
```